1 Page Website Design For Meridel Savings Card

~~I NEED A WEBSITE LANDING PAGE DESIGNED~~:

TITLE: GET UP TO 75% Off ALL YOUR DIABETIC SUPPLIES GUARANTEED
SUBITITLE: Never Pay Full Price For Your Diabetic Supplies Again!

~~FORM~~:
Choose Your Current Brand Of Diabetic Supplies That You Currently Use To See If They Are Covered Under Our Free Diabetic RX Assistance Program:

~~DROP DOWN MENU~~
Acarbose Up To 75% Off!

Verimbra Dux Up To 75% Off!

Verimbra Dux Xr Up To 54% Off!

Pelvo Up To 75% Off!

Borquell Up To 75% Off!

Tumisko Up To 75% Off!

Quisden Up To 75% Off!

Welvoke Up To 75% Off!

Zorpelline Up To 54% Off!

Zorpequin Up To 54% Off!

Zorpeta Up To 54% Off!

Calmivest Up To 75% Off!

Calmora Up To 75% Off!

Chlorpropamide Up To 75% Off!

Colesevelam Up To 75% Off!

Merrowin Up To 54% Off!

Qnrk Up To 75% Off!

Desmopressin 52% Off

Hostivel 74% Off

Pruntalex Up To 54% Off!
Sorvilk Up To 75% Off!

Delumbo Up To 75% Off!

Nuskavir Up To 75% Off!

Glimepiride 66% Off

Glipizide Up To 75% Off!

Glipizide Er Up To 75% Off!

Tremvalux Up To 75% Off!

Tremvalux Xr Up To 75% Off!

Brenzofil Up To 75% Off!

Brenzofil Xl Up To 75% Off!

Yestramor Up To 75% Off!

Kipolvan Up To 75% Off!

Glyburide Up To 75% Off!

Glyburide Micronized Up To 75% Off!
Ostrivel Up To 75% Off!

Pardow Up To 75% Off!

Vuntorek Up To 75% Off!

Restivon 50 50 Up To 75% Off!

Restivon Up To 75% Off!

Kavostra N Up To 75% Off!

Kavostra R Up To 75% Off!

Insulin Detemir Up To 75% Off!

Insulin Glulisine Up To 75% Off!

Pelsquorin Up To 75% Off!

Pelsquora Up To 75% Off!

Roblinex Up To 75% Off!

Roblinex Xr Up To 75% Off!

Roblivo Up To 75% Off!

Mespolure Up To 75% Off!

Wovrastelo Up To 75% Off!

Tilbemo Up To 75% Off!

Frastovane Xr Up To 75% Off!

Ovrink Up To 75% Off!

Sauprex Up To 75% Off!

Drunvelo Up To 54% Off!

Metformin 73% Off

Pastoquil Up To 54% Off!

Miglitol Up To 75% Off!

Ferbalick Up To 33% Off!

Nateglinide Up To 75% Off!

Ulvoria Up To 75% Off!

Zestrapol Up To 75% Off!

Zestrabin N Up To 75% Off!

Zestrabin R Up To 75% Off!

Zestrakor Up To 75% Off!

Zestraplum Up To 33% Off!

Brumvexa Up To 75% Off!

Tescavil Up To 54% Off!

Krudal Up To 75% Off!

Pioglitazone Up To 75% Off!

Pramlintide Up To 75% Off!

Wolbanix Up To 54% Off!

Wolbary Up To 75% Off!

Humbrek 20% Off

Repaglinide Up To 75% Off!

Sadvex Up To 75% Off!

Rosiglitazone Up To 75% Off!

Sitagliptin Up To 75% Off!

Plumvoy Up To 75% Off!

Garvostek Up To 75% Off!

Treskuvo Up To 75% Off!

Obrilcha Up To 75% Off!

Tolazamide Up To 75% Off!

Tolbutamide Up To 75% Off!

Vempruka Up To 54% Off!

Faskid Up To 75% Off!

Lurmobixa Up To 75% Off!

Qualmedo Up To 75% Off!

Sombrewick Up To 15% Off!

Vantoberry Up To 75% Off!

Dombrisel Up To 33% Off!

Harnupex Up To 75% Off!

Pidsarn Up To 75% Off!

Brafmel Xr Up To 75% Off!

~~~~After they choose one I want this message to pop up~~~~:

YES! ~~NAME OF DRUG~~ IS COVERED UNDER OUR FREE DIABETIC RX PROGRAM!
3 EASY WAYS TO RECEIVE YOUR FREE DIABETIC RX ASSISTANCE VOUCHER:

1. Simply Click Below To Download Your Voucher Right Now!

~~DOWNLOAD VOUCHER NOW~~
2. Enter Your Cell Phone Number And We Will Send The Voucher To You By Text Message Instantly:

3. Enter Your Email And We Will Send The Voucher To Your Email Instantly:

Target Market(s)

People with Diabetes

Number of Pages Required

1 page

Colors

Designer to choose colors to be used in the design.

Requirements
Must have
• must be professional looking and build trust and credibility
Nice to have
• Photos of diabetics...real people
Should not have
• red

```html
<!DOCTYPE html>
<html lang="en">
<head>
<meta charset="utf-8">
<title>Meridel Savings Card</title>
<link href="https://fonts.googleapis.com/css2?family=Poppins:wght@400;500;600&display=swap" rel="stylesheet">
<style>
  :root {
    --teal: #0a8fb4;
    --teal-bar: #0b92b8;
    --white: #ffffff;
    --list-bg: #efefef;
    --list-text: #444444;
    --scroll-track: #e2e2e2;
    --scroll-thumb: #c4c4c4;
  }
  * { box-sizing: border-box; margin: 0; padding: 0; }
  html, body { width: 1200px; height: 663px; overflow: hidden; }
  body { font-family: 'Poppins', sans-serif; color: var(--white); position: relative; }

  .hero-photo {
    position: absolute; inset: 0;
    background:
      linear-gradient(rgba(70,80,95,0.35), rgba(70,80,95,0.35)),
      linear-gradient(180deg, #8f9fae 0%, #7d8e9d 25%, #9aa3a9 45%, #b5b0a8 60%, #a59d95 80%, #8d8a8a 100%);
  }

  .menu-toggle {
    position: absolute; top: 43px; right: 57px;
    display: flex; align-items: center; gap: 9px;
    font-size: 14.5px; font-weight: 400; letter-spacing: 0.2px;
  }
  .menu-toggle svg { display: block; }

  .hero-content { position: absolute; top: 0; left: 0; width: 1200px; text-align: center; }
  .brand-name {
    position: absolute; top: 132px; width: 100%;
    font-size: 33px; font-weight: 600; letter-spacing: 2px;
    text-transform: uppercase;
  }
  .headline {
    position: absolute; top: 210px; width: 100%;
    font-size: 35px; font-weight: 600; letter-spacing: 0.3px;
  }
  .subheadline {
    position: absolute; top: 276px; width: 100%;
    font-size: 29.5px; font-weight: 500; line-height: 50px;
  }
  .form-prompt {
    position: absolute; top: 406px; width: 100%;
    font-size: 15.5px; font-weight: 400;
  }

  .brand-select {
    position: absolute; top: 464px; left: 463px; width: 275px;
    font-size: 12.5px;
  }
  .brand-select__current {
    height: 32px; background: var(--teal);
    display: flex; align-items: center; justify-content: space-between;
    padding: 0 10px 0 16px; font-weight: 500;
  }
  .brand-select__list {
    position: relative; height: 107px; background: var(--list-bg);
    list-style: none; padding-top: 4px; color: var(--list-text);
  }
  .brand-select__list li { height: 25.7px; line-height: 25.7px; padding-left: 16px; }
  .brand-select__scroll {
    position: absolute; top: 0; right: 0; width: 12px; height: 100%;
    background: var(--scroll-track);
  }
  .brand-select__thumb {
    position: absolute; top: 3px; left: 3px; width: 5px; height: 36px;
    background: var(--scroll-thumb); border-radius: 2px;
  }

  .site-footer {
    position: absolute; left: 0; bottom: 0; width: 1200px; height: 46px;
    background: var(--teal-bar);
    display: flex; align-items: center; justify-content: space-between;
    padding: 0 75px 0 40px;
  }
  .footer-nav { display: flex; align-items: center; font-size: 12.5px; font-weight: 500; }
  .footer-nav .sep { margin: 0 9px; }
  .copyright { font-size: 10.5px; font-weight: 600; }
</style>
</head>
<body>
  <div class="hero-photo" role="img" aria-label="Photo of a smiling older couple walking on a sunny beach"></div>

  <div class="menu-toggle">
    <span>MENU</span>
    <svg width="18" height="15" viewBox="0 0 18 15" aria-hidden="true">
      <rect x="0" y="0" width="18" height="3" rx="1" fill="#fff"/>
      <rect x="0" y="6" width="18" height="3" rx="1" fill="#fff"/>
      <rect x="0" y="12" width="18" height="3" rx="1" fill="#fff"/>
    </svg>
  </div>

  <main class="hero-content">
    <h1 class="brand-name">Meridel Savings Card</h1>
    <h2 class="headline">GET UP TO 75% OFF ALL YOUR DIABETIC SUPPLIES</h2>
    <p class="subheadline">Never Pay Full Price For Your Diabetic<br>Supplies Again!</p>
    <p class="form-prompt">Choose Your Current Brand Of Diabetic Supplies That You Currently Use To See If They Are Covered</p>
  </main>

  <div class="brand-select">
    <div class="brand-select__current">
      <span>Acarbose Up To 75% Off!</span>
      <svg width="10" height="6" viewBox="0 0 10 6" aria-hidden="true"><path d="M0 0h10L5 6z" fill="#fff"/></svg>
    </div>
    <div class="brand-select__list">
      <ul>
        <li>Verimbra Dux Up To 75% Off!</li>
        <li>Tumisko Up To 75% Off!</li>
        <li>Chlorpropamide Up To 75% Off!</li>
        <li>Colesevelam Up To 75% Off!</li>
      </ul>
      <div class="brand-select__scroll"><div class="brand-select__thumb"></div></div>
    </div>
  </div>

  <footer class="site-footer">
    <nav class="footer-nav">
      <span>About Us</span><span class="sep">|</span>
      <span>FAQ</span><span class="sep">|</span>
      <span>About Our Savings</span><span class="sep">|</span>
      <span>Affiliates</span><span class="sep">|</span>
      <span>Contact Us</span><span class="sep">|</span>
      <span>Privacy Policy</span><span class="sep">|</span>
      <span>Mobile</span>
    </nav>
    <p class="copyright">© 2017 Meridel Savings Card. All Rights Reserved.</p>
  </footer>
</body>
</html>
```